Display Ad for Local Publication

We have never advertised before but now I would like to have an ad running in our local, community magazine. Our business is Brackwater Mini Storage located in Cedar Inlet, WA. PL is a small community (+/-2,500 people located across the Puget Sound from Seattle. The monthly magazine, The Herald, covers all kinds of local news and activities and carries a number of ads from local businesses. Our is the only mini storage in Cedar Inlet. We have enclosed storage units of various sizes and outdoor parking spaces for boats, trailers and RVs. I am enclosing a business card and the size requirements for Herald advertisements. I want to develop a 1/8 page ad.

```html
<!DOCTYPE html>
<html lang="en">
<head>
<meta charset="utf-8">
<title>Brackwater Mini Storage – Display Ad</title>
<link href="https://fonts.googleapis.com/css2?family=Bitter:wght@700&family=Lato:ital,wght@1,700&display=swap" rel="stylesheet">
<style>
  :root {
    --brand-green: #52bb6f;
    --ink-grey: #58585a;
    --paper: #ffffff;
    --rule: #a9a9a9;
  }
  * { margin: 0; padding: 0; box-sizing: border-box; }
  html, body { width: 1200px; height: 829px; overflow: hidden; background: var(--paper); }
  .ad {
    position: relative;
    width: 1200px;
    height: 829px;
    background: var(--paper);
    font-family: "Lato", Arial, sans-serif;
    color: var(--ink-grey);
  }
  .ad-header {
    position: absolute; left: 0; top: 0;
    width: 1200px; height: 198px;
    background: var(--brand-green);
    display: flex; align-items: center; justify-content: center;
  }
  .business-name {
    font-family: "Bitter", Georgia, serif;
    font-weight: 700;
    font-size: 84px;
    color: var(--paper);
    letter-spacing: 0.5px;
  }
  .tagline {
    position: absolute; left: 68px; top: 262px;
    width: 517px; height: 146px;
    background: var(--ink-grey);
    color: var(--paper);
    font-family: "Bitter", Georgia, serif;
    font-weight: 700;
    font-size: 44px;
    line-height: 52px;
    padding: 20px 0 0 22px;
  }
  .contact-list {
    position: absolute; left: 68px; top: 480px;
    list-style: none;
  }
  .contact-item {
    display: flex; align-items: flex-start;
    font-style: italic; font-weight: 700;
    font-size: 37px; line-height: 48px;
    margin-bottom: 13px;
  }
  .contact-icon { width: 34px; height: 34px; margin: 7px 22px 0 0; flex: none; }
  .feature-list {
    position: absolute; left: 640px; top: 250px;
    width: 535px; list-style: none;
  }
  .feature {
    display: flex; align-items: center;
    height: 124px;
    border-bottom: 2px solid var(--rule);
  }
  .feature:last-child { border-bottom: none; }
  .feature-icon { width: 80px; height: 64px; flex: none; margin-right: 16px; }
  .feature-text {
    font-style: italic; font-weight: 700;
    font-size: 37px; line-height: 46px;
  }
  .ad-footer {
    position: absolute; left: 0; bottom: 0;
    width: 1200px; height: 20px;
    background: var(--ink-grey);
  }
</style>
</head>
<body>
<main class="ad">
  <header class="ad-header">
    <h1 class="business-name">Brackwater Mini Storage</h1>
  </header>

  <p class="tagline">Secure, Local &amp;<br>Convenient Storage</p>

  <ul class="contact-list">
    <li class="contact-item">
      <svg class="contact-icon" viewBox="0 0 34 34" fill="none" stroke="var(--brand-green)" stroke-width="2.5">
        <circle cx="17" cy="17" r="15"/>
        <path d="M11 10c-1 3 1 8 5 12s8 5 9 3l-1-3-3-1-2 2c-2-1-4-3-5-5l2-2-1-3z" fill="var(--brand-green)" stroke="none"/>
      </svg>
      <span>360-555-0147</span>
    </li>
    <li class="contact-item">
      <svg class="contact-icon" viewBox="0 0 34 34" fill="none" stroke="var(--brand-green)" stroke-width="2.5">
        <circle cx="17" cy="17" r="15"/>
        <rect x="9" y="11" width="16" height="12" rx="1" fill="var(--brand-green)" stroke="none"/>
        <path d="M9 12l8 6 8-6" stroke="var(--paper)" stroke-width="1.8"/>
      </svg>
      <span>bwministorage@mailbox.com</span>
    </li>
    <li class="contact-item">
      <svg class="contact-icon" viewBox="0 0 34 34" fill="none" stroke="var(--brand-green)" stroke-width="2.5">
        <circle cx="17" cy="17" r="15"/>
        <path d="M17 26s-6-6-6-11a6 6 0 0 1 12 0c0 5-6 11-6 11z" fill="var(--brand-green)" stroke="none"/>
        <circle cx="17" cy="15" r="2.2" fill="var(--paper)" stroke="none"/>
      </svg>
      <span>218 Harbor Crest Way,<br>Cedar Inlet, WA</span>
    </li>
  </ul>

  <ul class="feature-list">
    <li class="feature">
      <svg class="feature-icon" viewBox="0 0 80 64" fill="var(--brand-green)">
        <path d="M40 6l26 10-26 10-26-10z"/>
        <path d="M12 20l26 10v30L12 50z"/>
        <path d="M68 20L42 30v30l26-10z"/>
        <path d="M28 12l26 10v8l-6 2v-8L22 14z" fill="var(--paper)" opacity="0.5"/>
      </svg>
      <span class="feature-text">Clean enclosed units<br>–multiple sizes</span>
    </li>
    <li class="feature">
      <svg class="feature-icon" viewBox="0 0 80 64" fill="none" stroke="var(--brand-green)" stroke-width="3" stroke-linejoin="round">
        <path d="M14 36h52l-8 10H22z"/>
        <path d="M30 36l6-10h14l6 10"/>
        <path d="M2 50h70"/>
        <circle cx="50" cy="52" r="5" fill="var(--paper)"/>
      </svg>
      <span class="feature-text">Outdoor parking for<br>boats, &amp; RVs</span>
    </li>
    <li class="feature">
      <svg class="feature-icon" viewBox="0 0 80 64" fill="none" stroke="var(--brand-green)" stroke-width="3">
        <path d="M22 60V14l20-8 20 8v46"/>
        <rect x="30" y="26" width="24" height="30" fill="var(--brand-green)" stroke="none"/>
        <path d="M34 34h16M34 40h16M34 46h16" stroke="var(--paper)" stroke-width="2.5"/>
      </svg>
      <span class="feature-text">The only mini storage<br>facility in Cedar Inlet</span>
    </li>
    <li class="feature">
      <svg class="feature-icon" viewBox="0 0 80 64" fill="none" stroke="var(--brand-green)" stroke-width="4">
        <path d="M30 28V18a10 10 0 0 1 20 0v10"/>
        <rect x="24" y="28" width="32" height="32" rx="6" fill="var(--brand-green)" stroke="none"/>
        <circle cx="40" cy="44" r="9" stroke="var(--paper)" stroke-width="2.5"/>
        <path d="M35 44l4 4 6-7" stroke="var(--paper)" stroke-width="2.5"/>
      </svg>
      <span class="feature-text">Safe, accessible and<br>locally owned</span>
    </li>
  </ul>

  <footer class="ad-footer"></footer>
</main>
</body>
</html>
```